Premium Personal Brand — Facebook Banner (Used Across All Platforms)

Update — Additional Color Direction
In addition to the dark charcoal/slate direction already described, I'm also interested in seeing variants with:
Dark navy blue — Deep, authoritative, intelligence-community feel. Same textured/matte treatment, not flat or bright.
Warm charcoal with steel blue accent — Keep the dark base but introduce a subtle steel blue gradient, accent line, or tonal shift. Sophisticated, modern, adds dimension without adding color noise.
Both should maintain the same premium, restrained, architectural feel described in the original brief. No bright blues, no corporate PowerPoint energy — think midnight, think depth, think weight.
Everything else in the brief remains the same.
I am building a premium personal brand as an executive advisor to founders ($5M+ revenue).
This contest is Facebook-banner–focused, but the design must represent a visual system that will be reused across:
- LinkedIn
- YouTube
I- nstagram
- X (Twitter)
- Website hero sections and other brand touchpoints
Think of the Facebook banner as the primary expression of the brand — not a one-off graphic.
This project is about discovering a high-end visual style and brand feel, not decoration.
What to design
Please submit one cohesive visual system, shown primarily as:
- Facebook banner (primary focus)
The same design language should clearly translate to all platforms listed above.
Designers are responsible for using the current recommended dimensions for each platform.
Quick clarification on background direction:
Backgrounds should have depth and texture, not flat color fields. Avoid pure white, light grey, or solid black backgrounds. Think matte, architectural materials — stone, graphite, concrete, steel — not blank canvases. Subtle tonal variation is encouraged. Obvious gradients or decorative patterns are not.
Text to use
Primary Headline:
- Your Business Is Too Valuable To Be Run On Hope.
Subheadline:
- You didn’t build a business to become its prisoner.
Name:
Paul Whitaker
The headline should be the dominant visual element.
Logo note (important)
My personal logo is currently being finalized.
For this contest:
- Use a simple “PW” monogram placeholder
- Clean, bold, geometric sans-serif
- Do not design a logo
- The winning design must allow an easy logo swap later.
Headshot note (important)
- Please do not include a headshot in the banner design.
- Most platforms display a circular profile image separately.
- The banner should stand on its own using typography, layout, and tone only.
- Design the banner assuming the profile photo will sit nearby, not inside the banner.
Style direction
The design should feel:
- Premium
- Calm
- Confident
- Restrained
- High-trust
- Dark, neutral backgrounds are preferred.
- Fewer elements are better than more.
Think:
- Owner-level advisor
- Private equity / boardroom tone
- Industrial, Modern, Minimalist, Elite, Architectural, not decorative
What to avoid
Please do not submit designs that feel:
- Promotional, hype-driven, or salesy
- Like a coach, guru, or agency
- Bright, colorful, or gradient-heavy
- Busy or over-designed
- Based on stock photos
- No motivational speaker energy.
Reaction test
- If someone sees this banner on Facebook (or later on LinkedIn, YouTube, etc.), the reaction should be:
“That person is serious. I’d trust them with important decisions.”
Final note
- I am not looking for many variations.
- I am looking for one strong visual direction you believe in.
Simple beats clever.
- Restraint beats decoration.

```html
<!DOCTYPE html>
<html lang="en">
<head>
<meta charset="utf-8">
<title>Paul Whitaker — Banner</title>
<link href="https://fonts.googleapis.com/css2?family=Montserrat:wght@300;800&display=swap" rel="stylesheet">
<style>
  :root {
    --ink: #050808;
    --stone-deep: #3d6f78;
    --stone-mid: #5b8f97;
    --stone-light: #86b2b8;
    --stone-haze: #a3c6ca;
    --stone-shadow: #2f5a62;
  }
  html, body {
    margin: 0;
    padding: 0;
    width: 1200px;
    height: 457px;
    overflow: hidden;
    background: var(--stone-mid);
  }
  .banner {
    position: relative;
    width: 1200px;
    height: 457px;
    overflow: hidden;
    font-family: "Montserrat", sans-serif;
    color: var(--ink);
  }
  .banner__texture {
    position: absolute;
    inset: 0;
    width: 100%;
    height: 100%;
  }
  .headline {
    position: absolute;
    left: 62px;
    top: 50px;
    margin: 0;
    font-weight: 800;
    font-size: 85px;
    line-height: 80px;
    letter-spacing: -1.5px;
    white-space: nowrap;
  }
  .subheadline {
    position: absolute;
    left: 63px;
    top: 329px;
    margin: 0;
    font-weight: 300;
    font-size: 42px;
    line-height: 44px;
    letter-spacing: 0.5px;
    white-space: nowrap;
  }
  .monogram {
    position: absolute;
    right: 56px;
    top: 262px;
    margin: 0;
    font-weight: 800;
    font-size: 178px;
    line-height: 1;
    letter-spacing: -6px;
  }
</style>
</head>
<body>
<main class="banner">
  <svg class="banner__texture" viewBox="0 0 1200 457" preserveAspectRatio="none" role="img" aria-label="Matte weathered teal stone texture background">
    <defs>
      <linearGradient id="stone-base" x1="0" y1="0" x2="1" y2="1">
        <stop offset="0" stop-color="var(--stone-light)"/>
        <stop offset="0.5" stop-color="var(--stone-mid)"/>
        <stop offset="1" stop-color="var(--stone-deep)"/>
      </linearGradient>
      <radialGradient id="stone-haze" cx="0.88" cy="0.05" r="0.45">
        <stop offset="0" stop-color="var(--stone-haze)" stop-opacity="0.8"/>
        <stop offset="1" stop-color="var(--stone-haze)" stop-opacity="0"/>
      </radialGradient>
      <radialGradient id="stone-shade" cx="0.6" cy="1" r="0.55">
        <stop offset="0" stop-color="var(--stone-shadow)" stop-opacity="0.45"/>
        <stop offset="1" stop-color="var(--stone-shadow)" stop-opacity="0"/>
      </radialGradient>
    </defs>
    <rect width="1200" height="457" fill="url(#stone-base)"/>
    <rect width="1200" height="457" fill="url(#stone-haze)"/>
    <rect width="1200" height="457" fill="url(#stone-shade)"/>
  </svg>

  <h1 class="headline">Your business is<br>too valuable to be<br>run on hope.</h1>
  <p class="subheadline">You didn’t build a business<br>to become its prisoner.</p>
  <p class="monogram" aria-label="Paul Whitaker">PW</p>
</main>
</body>
</html>
```